Not-for-profit Community Law Business Card

Not-for-Profit community law firm are looking for new business card design to accompany a new logo.
The cards are to assist the organisation in reaching their strategic objective of generating greater networking amongst the community; specifically with other service providers, clients, and community influencers.
It should stand out. Be professional, strong, creative, clear in detail. The logo should be a major feature of the design.
Updates

Hi All,

Thank you for the submissions so far. I have uploaded the logo and colour details again, as requested. If you have any further issues downloading them or need a different format please contact me on jess_harlow@bvm.net.au

Kind regards,

Industry/Entity Type

Law Firm

Requirements
Must have
• Logo (attached)
Person's name
Position
Phone
Fax
Email
PO Box address
Website
Colours from the logo.

```html
<!DOCTYPE html>
<html lang="en">
<head>
<meta charset="utf-8">
<title>Westmere Advocacy Law Service – Business Card</title>
<link rel="stylesheet" href="https://fonts.googleapis.com/css2?family=Michroma&display=swap">
<style>
  :root {
    --page-bg: #dfe7ee;
    --card-bg: #ffffff;
    --brand-blue: #1f6fb8;
    --brand-navy: #2b4a9a;
    --pattern-tint: #eef1f9;
    --card-shadow: rgba(40, 70, 100, 0.18);
  }
  * { margin: 0; padding: 0; box-sizing: border-box; }
  html, body {
    width: 1000px;
    height: 1200px;
    overflow: hidden;
    background: var(--page-bg);
    font-family: "Michroma", sans-serif;
  }
  .canvas {
    position: relative;
    width: 1000px;
    height: 1200px;
  }
  .business-card {
    position: absolute;
    left: 216px;
    top: 452px;
    width: 568px;
    height: 310px;
    background: var(--card-bg);
    box-shadow: 0 10px 30px var(--card-shadow);
    overflow: hidden;
  }
  .icon-pattern {
    position: absolute;
    left: 20px;
    top: 0;
    width: 548px;
    height: 310px;
    background: radial-gradient(ellipse at 60% 50%, var(--pattern-tint), var(--card-bg) 80%);
  }
  .brand-dot {
    position: absolute;
    left: 2px;
    top: 8px;
    width: 50px;
    height: 50px;
    border-radius: 50%;
    background: var(--brand-blue);
  }
  .brand-name {
    position: absolute;
    left: 62px;
    top: 30px;
    color: var(--brand-navy);
    font-variant: small-caps;
    font-size: 15px;
    line-height: 18px;
    letter-spacing: 0;
    white-space: nowrap;
  }
  .brand-name .sub {
    display: block;
    font-size: 11px;
    line-height: 16px;
    padding-left: 86px;
  }
  .contact-block {
    position: absolute;
    left: 184px;
    top: 90px;
    color: var(--brand-blue);
    font-variant: small-caps;
  }
  .person-name {
    font-size: 21px;
    letter-spacing: 0.08em;
    line-height: 30px;
    color: var(--brand-navy);
  }
  .person-position {
    font-size: 15px;
    letter-spacing: 0.06em;
    line-height: 24px;
    margin-bottom: 4px;
  }
  .contact-list { list-style: none; }
  .contact-item {
    display: flex;
    align-items: center;
    height: 25.5px;
    font-size: 12.5px;
    letter-spacing: 0.1em;
    white-space: nowrap;
  }
  .contact-icon {
    width: 20px;
    height: 20px;
    margin-right: 8px;
    fill: var(--brand-blue);
    flex: none;
  }
  .contact-item.no-icon { padding-left: 28px; }
</style>
</head>
<body>
<div class="canvas">
  <div class="business-card">
    <div class="icon-pattern" role="img" aria-label="Faint pattern of legal icons: gavels, scales, courthouses, books and documents"></div>

    <span class="brand-dot"></span>
    <p class="brand-name">Westmere Advocacy<span class="sub">Law Service Inc.</span></p>

    <div class="contact-block">
      <p class="person-name">Your Name</p>
      <p class="person-position">Position</p>
      <ul class="contact-list">
        <li class="contact-item">
          <svg class="contact-icon" viewBox="0 0 20 20"><path d="M4 2l3 0 1.5 4-2 1.5c1 2.2 2.8 4 5 5l1.5-2 4 1.5v3c0 1-1 2-2 2C8 17 3 12 2 4c0-1 1-2 2-2z"/></svg>
          (123)-456-7890
        </li>
        <li class="contact-item">
          <svg class="contact-icon" viewBox="0 0 20 20"><rect x="1" y="7" width="4" height="11" rx="1"/><rect x="6" y="2" width="10" height="6"/><rect x="6" y="8" width="13" height="10" rx="1"/><rect x="8" y="10" width="2" height="2" fill="#fff"/><rect x="12" y="10" width="2" height="2" fill="#fff"/><rect x="8" y="14" width="2" height="2" fill="#fff"/><rect x="12" y="14" width="2" height="2" fill="#fff"/></svg>
          (098)-765-4321
        </li>
        <li class="contact-item">
          <svg class="contact-icon" viewBox="0 0 20 20"><path d="M1 4h18v12H1z M3 6v8h14V6l-7 5z M3.5 5.5L10 10l6.5-4.5z" fill-rule="evenodd"/></svg>
          contact@email.com
        </li>
        <li class="contact-item">
          <svg class="contact-icon" viewBox="0 0 20 20"><path d="M10 2l9 8h-3v8h-4v-5H8v5H4v-8H1z"/></svg>
          PO Box
        </li>
        <li class="contact-item no-icon">Address</li>
        <li class="contact-item">
          <svg class="contact-icon" viewBox="0 0 20 20"><circle cx="10" cy="10" r="9"/><g fill="none" stroke="#fff" stroke-width="1.2"><ellipse cx="10" cy="10" rx="4" ry="9"/><path d="M1 10h18M3 5.5h14M3 14.5h14M10 1v18"/></g></svg>
          http://www.westmereadvocacy.org
        </li>
      </ul>
    </div>
  </div>
</div>
</body>
</html>
```